Marlow Crest Holdings (Remodeling company) needs a logo and business card

We need a business card design for a new company. We "flip" upmarket houses (buy, remodel and sell) in the Austin, TX area. I'd like neutral colors (grey, white, gold black). I would like it to include a simple, clean logo. Our designs are modern and uncluttered and I would like that reflected in the business card design.

Target Market(s)

Young professionals, Families, Retirees. Our properties will sell for $750k+

Industry/Entity Type

Real Estate

Contact Information for Business Card

Marlow Crest Holdings
Nora Pellham
(555) 216 7042
Owner
Rory Tansil
(555) 638 1975
Realtor

Logo Text

Marlow Crest Holdings

Font styles to use
Serif
Script

Requirements
Must have
• Simple, classic design
Nice to have
• Clean lines, modern look
Should not have
• Too traditionally

```html
<!DOCTYPE html>
<html lang="en">
<head>
<meta charset="UTF-8">
<title>Marlow Crest Holdings – Business Card</title>
<link rel="stylesheet" href="https://fonts.googleapis.com/css2?family=Josefin+Sans:wght@300;400&display=swap">
<style>
  :root {
    --backdrop: #ededed;
    --card-white: #f8f7f7;
    --panel-light: #ececec;
    --panel-mid: #d9d9d9;
    --ink: #1e1e1e;
    --ink-soft: #333333;
    --accent-blue: #2188bd;
    --icon-ink: #111111;
  }

  * { box-sizing: border-box; margin: 0; padding: 0; }

  html, body {
    width: 1200px;
    height: 799px;
    overflow: hidden;
    background: var(--backdrop);
    font-family: "Josefin Sans", "Helvetica Neue", Arial, sans-serif;
    color: var(--ink);
  }

  .card {
    position: absolute;
    left: 180px;
    top: 161px;
    width: 840px;
    height: 476px;
    display: flex;
    background: var(--card-white);
    box-shadow: 0 6px 18px rgba(0, 0, 0, 0.12);
  }

  .card__brand {
    position: relative;
    width: 418px;
    height: 100%;
    display: flex;
    align-items: center;
    justify-content: center;
    background: var(--card-white);
  }

  .brand-name {
    text-align: center;
    font-weight: 300;
    font-size: 44px;
    line-height: 1.05;
    letter-spacing: 1px;
    text-transform: uppercase;
    color: var(--ink-soft);
    margin-top: 90px;
  }

  .card__contacts {
    position: relative;
    flex: 1;
    height: 100%;
    background: radial-gradient(ellipse at 65% 40%, var(--panel-light) 0%, var(--panel-mid) 100%);
    padding: 104px 0 0 52px;
  }

  .card__contacts::before {
    content: "";
    position: absolute;
    left: -38px;
    top: 104px;
    width: 0;
    height: 0;
    border-top: 26px solid transparent;
    border-bottom: 26px solid transparent;
    border-right: 38px solid #dadada;
  }

  .contact + .contact { margin-top: 46px; }

  .contact__name {
    font-size: 33px;
    font-weight: 400;
    line-height: 1.1;
    color: var(--ink);
  }

  .contact__role {
    font-size: 24px;
    font-weight: 300;
    text-transform: uppercase;
    line-height: 1.2;
    margin-top: 4px;
    color: var(--ink);
  }

  .contact__phone {
    display: flex;
    align-items: center;
    gap: 20px;
    margin-top: 18px;
    font-size: 17px;
    font-weight: 400;
    letter-spacing: 0.5px;
    color: var(--ink-soft);
  }

  .phone-icon { width: 28px; height: 28px; flex: none; }

  .card__band {
    position: absolute;
    left: 0;
    right: 0;
    bottom: 0;
    height: 33px;
    background: var(--accent-blue);
  }
</style>
</head>
<body>
  <div class="card">
    <section class="card__brand">
      <p class="brand-name">Marlow Crest<br>Holdings</p>
    </section>

    <section class="card__contacts">
      <div class="contact">
        <p class="contact__name">Nora Pellham</p>
        <p class="contact__role">Owner</p>
        <p class="contact__phone">
          <svg class="phone-icon" viewBox="0 0 28 28" aria-hidden="true">
            <rect width="28" height="28" fill="var(--icon-ink)"/>
            <path d="M6 11c0-3 4-4 8-4s8 1 8 4l-3 1-1-2c-2-1-6-1-8 0l-1 2z" fill="#fff"/>
            <path d="M9 13h10l2 8H7z" fill="#fff"/>
            <circle cx="14" cy="17" r="2" fill="var(--icon-ink)"/>
          </svg>
          (555) 216 7042
        </p>
      </div>

      <div class="contact">
        <p class="contact__name">Rory Tansil</p>
        <p class="contact__role">Realtor</p>
        <p class="contact__phone">
          <svg class="phone-icon" viewBox="0 0 28 28" aria-hidden="true">
            <rect width="28" height="28" fill="var(--icon-ink)"/>
            <path d="M6 11c0-3 4-4 8-4s8 1 8 4l-3 1-1-2c-2-1-6-1-8 0l-1 2z" fill="#fff"/>
            <path d="M9 13h10l2 8H7z" fill="#fff"/>
            <circle cx="14" cy="17" r="2" fill="var(--icon-ink)"/>
          </svg>
          (555) 638 1975
        </p>
      </div>

      <div class="card__band"></div>
    </section>
  </div>
</body>
</html>
```